Social Business Consultancy

Kavora Ventures is a start up consultancy but with a difference: were non-corporate. We work in the field of economic development in low income countries and we focus on entrepreneurship but with a social and or environmental mission.

The type of projects we work on are innovative, ground breaking, different, edgy and bold. We are young, determined, , unreasonnable and undeterred by challenges.
We want our website to convey these ideas.
Updates

Hello,

Could you please include the option of having the website in two languages. Thank you.

Please note that new files have been added to the project brief.

- FrontPage  Main Photo (Grey dirt Road)
- WordCloud Photo to be used on the home page (as a small image )

The website should keep these colour tones.

Thank you !

Hello,

Wireframes have been uploaded. Please use as an indication.

Thanks,
n.

Target Market(s)

Governments, development agencies, social investors, NGOs, banks and social entrepreneurs.

Industry/Entity Type

Consulting

Requirements
Must have
• We already have a logo and business cards (provided). We want the website to look professional, yet simple with a maximum of two or three colours. We want the look to be seamless. There is no need for too many boxes or categories.
Nice to have
• We want bold, edgy, modern  and professional look .
• Examples:
• http://www.brightmarrowlab.org/
• http://www.pavelstone.com/
• http://www.tarnhiring.co.nz/
Should not have
• The design should not use old style fonts.

```html
<!DOCTYPE html>
<html lang="en">
<head>
<meta charset="utf-8">
<title>Kavora Ventures</title>
<link rel="stylesheet" href="https://fonts.googleapis.com/css2?family=Arimo:wght@400;700&family=Kaushan+Script&display=swap">
<style>
  :root {
    --bg-top: #221e1c;
    --bg-bottom: #504a47;
    --rule: #8a8583;
    --tab: #1d1a19;
    --frame: #6b6664;
    --panel-outer: #3b3735;
    --panel-inner: #4a4542;
    --card: #5d5552;
    --button: #787270;
    --footer: #2d2a29;
    --text: #f2f2f2;
    --muted: #d9d9d9;
    --accent: #5fd3e4;
    --wordmark: #e6e6e6;
  }
  * { box-sizing: border-box; margin: 0; padding: 0; }
  html, body { width: 1200px; height: 1152px; overflow: hidden; }
  body {
    position: relative;
    font-family: "Arimo", Arial, sans-serif;
    color: var(--text);
    background: linear-gradient(180deg, var(--bg-top) 0%, #2c2724 25%, #3f3936 70%, var(--bg-bottom) 100%);
  }
  a { color: inherit; text-decoration: none; }

  .brand {
    position: absolute; left: 72px; top: 58px;
    font-family: "Arimo", Arial, sans-serif; font-weight: 700; font-size: 58px; line-height: 1;
    color: var(--wordmark);
  }

  .quick-links { position: absolute; top: 20px; left: 925px; display: flex; gap: 46px; }
  .quick-link { display: flex; flex-direction: column; align-items: center; font-size: 18px; font-weight: 700; }
  .quick-link .icon { height: 56px; border-radius: 8px; margin-bottom: 4px; }
  .icon-about { width: 96px; background: linear-gradient(90deg, #3f63a8 0 48%, transparent 48% 52%, #c9453a 52%); border-radius: 28px 28px 6px 6px; }
  .icon-contact { width: 56px; background: linear-gradient(180deg, #6a6a6a, #1a1a1a); border: 1px solid #999; }

  .main-nav {
    position: absolute; left: 615px; top: 144px; width: 553px; height: 43px;
    background: var(--tab); border-radius: 6px 6px 0 0;
    display: flex; justify-content: center; align-items: center; gap: 12px;
    font-size: 16px;
  }
  .header-rule { position: absolute; left: 0; top: 187px; width: 1200px; height: 1px; background: var(--rule); }

  .hero {
    position: absolute; left: 41px; top: 205px; width: 1118px; height: 383px;
    border: 7px solid var(--frame); border-radius: 12px; overflow: hidden;
  }
  .hero-image {
    width: 100%; height: 100%;
    background: linear-gradient(180deg, #b9bcbd 0%, #8f9292 28%, #a59a74 32%, #c9b17a 50%, #b69462 75%, #8e7048 100%);
  }

  .language {
    position: absolute; right: 61px; top: 601px;
    font-size: 16px; display: flex; gap: 14px; align-items: center;
  }
  .language-label { font-weight: 700; color: var(--muted); letter-spacing: 0.5px; margin-right: 10px; }

  .content {
    position: absolute; left: 41px; top: 635px; width: 1120px; height: 389px;
    background: var(--panel-inner); border: 5px solid var(--panel-outer);
  }
  .card { position: absolute; top: 8px; background: var(--card); border-radius: 10px; }
  .welcome { left: 15px; width: 434px; height: 355px; padding: 12px 20px 0; }
  .news { left: 767px; width: 327px; height: 355px; padding: 12px 14px 0 20px; }
  .card-title { font-family: "Kaushan Script", cursive; font-weight: 400; font-size: 36px; color: var(--accent); line-height: 1.15; white-space: nowrap; }
  .card-title .name { font-family: "Arimo", sans-serif; font-size: 36px; }
  .card p { font-size: 15.5px; line-height: 24px; text-align: justify; hyphens: auto; margin-top: 6px; }
  .welcome p + p { margin-top: 24px; }
  .news p { margin-top: 30px; }
  .read-more {
    position: absolute; right: 20px; bottom: 6px;
    background: var(--button); font-size: 16px; line-height: 20px; padding: 0 6px;
  }
  .feature-photo {
    position: absolute; left: 469px; top: 8px; width: 280px; height: 356px; border-radius: 8px;
    background: linear-gradient(160deg, #1f3a6a 0%, #8aa0c4 35%, #e4ebf3 60%, #6f7b8e 85%, #121316 100%);
  }

  .footer-nav {
    position: absolute; left: 41px; top: 1056px; width: 1118px; height: 44px;
    background: var(--footer); border-radius: 12px;
    display: flex; justify-content: center; align-items: center; gap: 13px; font-size: 16px;
  }
  .sep { color: var(--muted); }
</style>
</head>
<body>
  <header>
    <div class="brand">Kavora</div>

    <div class="quick-links">
      <a class="quick-link" href="#about"><span class="icon icon-about" role="img" aria-label="Two team member icons"></span>About us</a>
      <a class="quick-link" href="#contact"><span class="icon icon-contact" role="img" aria-label="Headset contact icon"></span>Contact us</a>
    </div>

    <nav class="main-nav">
      <a href="#approach">Our Approach</a><span class="sep">|</span>
      <a href="#services">Our Services</a><span class="sep">|</span>
      <a href="#projects">Our Projects</a><span class="sep">|</span>
      <a href="#news">News &amp; Events</a>
    </nav>
    <div class="header-rule"></div>
  </header>

  <section class="hero">
    <div class="hero-image" role="img" aria-label="Dirt road running through dry golden grassland under a grey sky"></div>
  </section>

  <div class="language">
    <span class="language-label">Choose Language :</span>
    <a href="#en">Eng</a><span class="sep">|</span><a href="#fr">Fr</a>
  </div>

  <main class="content">
    <article class="card welcome">
      <h2 class="card-title">Welcome to <span class="name">Kavora</span></h2>
      <p>Established in 2006 TARN has been created by a local team to focus on a personalised fresh approach to recruitment with a select group of clients, candidates and employees.</p>
      <p>As a boutique agency specialising in dynamic industry sectors we recognise businesses in these industries cannot be properly serviced by a generalist recruiter. We actively seek the best available team all with relevant industry backgrounds to serve our clients and candidates in the industries in which they operate.</p>
      <a class="read-more" href="#more">Read More..</a>
    </article>

    <div class="feature-photo" role="img" aria-label="Silhouette of a person standing against a bright sky"></div>

    <article class="card news">
      <h2 class="card-title">News &amp; Events</h2>
      <p>As a boutique agency specialising in dynamic industry sectors we recognise businesses in these industries cannot be properly serviced by a generalist recruiter. We actively seek the best available team all with relevant industry backgrounds to serve our clients and candidates in the industries in which they operate.</p>
    </article>
  </main>

  <footer>
    <nav class="footer-nav">
      <a href="#home">Home</a><span class="sep">|</span>
      <a href="#about">About us</a><span class="sep">|</span>
      <a href="#approach">Our Approach</a><span class="sep">|</span>
      <a href="#services">Our Services</a><span class="sep">|</span>
      <a href="#projects">Our Projects</a><span class="sep">|</span>
      <a href="#news">News &amp; Events</a>
    </nav>
  </footer>
</body>
</html>
```